Label / Packaging design for supplements bottle (capsule bottle)

We are a startup supplements company focusing on animal nutrition. The task here is to design the supplement bottles for the product series. Think of bodybuilding supplement packaging more than health&wellness type of packaging.

The brandname is Perch Dynamics

The goal is to have 3 bottles with similar/identical designs but with different color accents (i.e. red for one bottle, yellow for the second, (not green or blue) for the third).

The bottles can either be black theme or white theme. I'll leave it up to the designer.

Final design should communicate bodybuilding (bold fonts preferred)

Logo files below (both SVG and AI files), the insignia can be used independently of the text and slogan, or it can be positioned above brand name or beside it.
*Feel free to change the color of the insignia and text to match your chosen accent color for the bottle!*

Bottle size will be approximately 11.9cm x 6.35cm (Height x circumference) (height is from bottom to mouth opening)
Thus, label size at the moment can be designed 6.30cm x 10cm (L x W)

Target Market(s)

Male, Adult

Industry/Entity Type

It Company

Font styles to use
Sans Serif

Requirements
Must have
• Text: "Performance Enhancing Supplements for Racing Pigeons"
• Essentials
• "240 Capsules"
• Bottle 1:
• Creatine+Carnitine
• Text + Imagery:*see Carnitine Benefits.png
• Bottle 2:
• BCAA
• Text:
• SUPPORT MUSCLE PROTEIN SYNTHESIS
• DECREASE PROTEIN CATABOLISM
• PROMOTE INSULIN SENSITIVITY
• Offset Muscle Breakdown and Increase Muscular Endurance
• ENHANCED RECOVERY FROM EXERCISE
• Promotes Lowered Body Fat Levels, Increased Strength, & Improves Muscle Repair
• (Imagery can use the same as bottle 1 similar to Carnitine Benefits.png)
• Bottle 3:
• Vitamins
• Text: Supports Rigorous Training and Needs To Support Growth and Overall Well-being
• Spaces for Text for:
• 1.) Directions for Use
• 2.) Developed by:
• 3.) Ingredients
Nice to have
• Mosaic/Pattern subtle fading background (e.g. honeycomb etc)
• Prominent "A" "B" "C" on each bottle,
• A for Bulwark Nutrients
• B for BCAA
• C for Taurine/Glutamine Complex
• XYZ Essential Series

```html
<!DOCTYPE html>
<html lang="en">
<head>
<meta charset="utf-8">
<title>Perch Dynamics – Vitamins Label</title>
<link rel="stylesheet" href="https://fonts.googleapis.com/css2?family=Orbitron:wght@700;900&family=Open+Sans:wght@700&display=swap">
<style>
  :root {
    --page: #eeeeee;
    --gold: #b5a82c;
    --gold-light: #f3e9a6;
    --gold-mid: #d8c25a;
    --gold-dark: #8a7a1c;
    --panel: #0b0b0b;
    --panel-soft: #1c1c1c;
    --white: #ffffff;
  }
  * { margin: 0; padding: 0; box-sizing: border-box; }
  html, body { width: 1200px; height: 823px; overflow: hidden; background: var(--page); }
  .label {
    position: absolute; left: 80px; top: 84px; width: 1040px; height: 655px;
    background: var(--panel); overflow: hidden;
  }
  .label__texture {
    position: absolute; inset: 0;
    background: radial-gradient(ellipse at 50% 65%, var(--panel-soft) 0%, var(--panel) 70%);
  }
  .band { position: absolute; left: 0; width: 100%; background: var(--gold); }
  .band--top { top: 0; height: 26px; }
  .band--bottom { bottom: 0; height: 27px; }
  .header-tab { position: absolute; left: 330px; top: 0; width: 380px; height: 77px; }
  .brand-name {
    position: absolute; left: 330px; top: 22px; width: 380px; text-align: center;
    font-family: "Orbitron", sans-serif; font-weight: 900; font-size: 27px;
    color: var(--white); letter-spacing: 0.5px;
  }
  .product-title {
    position: absolute; left: 0; top: 102px; width: 100%; text-align: center;
    font-family: "Orbitron", sans-serif; font-weight: 900; font-size: 90px; letter-spacing: 4px;
    line-height: 1;
    background: linear-gradient(180deg, var(--gold-light) 0%, var(--gold-mid) 50%, var(--gold-dark) 100%);
    -webkit-background-clip: text; background-clip: text; color: transparent;
    filter: drop-shadow(0 0 8px rgba(216, 194, 90, 0.6));
  }
  .tagline {
    position: absolute; left: 0; top: 205px; width: 100%; text-align: center;
    font-family: "Open Sans", sans-serif; font-weight: 700; font-size: 15px; color: var(--white);
  }
  .series {
    position: absolute; left: 394px; top: 234px; width: 259px; height: 52px;
    border: 3px solid var(--gold); display: flex; align-items: center; justify-content: center;
    font-family: "Orbitron", sans-serif; font-weight: 700; font-style: italic; font-size: 19px;
    color: var(--white);
  }
  .series-letter {
    position: absolute; left: 0; top: 292px; width: 100%; text-align: center;
    font-family: "Orbitron", sans-serif; font-weight: 900; font-style: italic; font-size: 92px; line-height: 1;
    background: linear-gradient(180deg, var(--gold-light) 0%, var(--gold-mid) 55%, var(--gold-dark) 100%);
    -webkit-background-clip: text; background-clip: text; color: transparent;
  }
  .benefit-band {
    position: absolute; left: 0; top: 406px; width: 100%; height: 130px;
    background: linear-gradient(90deg, rgba(0,0,0,0) 18%, rgba(181,168,44,0.85) 32%, rgba(138,122,28,0.45) 65%, rgba(0,0,0,0.15) 95%);
  }
  .brand-seal {
    position: absolute; left: 215px; top: 376px; width: 160px; height: 160px;
    border-radius: 50%; background: var(--white);
    display: flex; align-items: center; justify-content: center; text-align: center;
    font-family: "Orbitron", sans-serif; font-weight: 900; font-size: 17px; color: var(--gold-dark);
    line-height: 1.2;
  }
  .benefit-text {
    position: absolute; left: 420px; top: 420px; width: 520px;
    font-family: "Orbitron", sans-serif; font-weight: 700; font-style: italic; font-size: 22px;
    line-height: 33px; color: var(--white);
  }
  .capsule-badge { position: absolute; left: 424px; top: 554px; width: 184px; height: 101px; }
  .capsule-badge__count {
    position: absolute; left: 0; top: 22px; width: 100%; text-align: center;
    font-family: "Open Sans", sans-serif; font-weight: 700; font-size: 38px; color: var(--white); line-height: 1;
  }
  .capsule-badge__unit {
    position: absolute; left: 0; top: 68px; width: 100%; text-align: center;
    font-family: "Open Sans", sans-serif; font-weight: 700; font-size: 18px; color: var(--white);
  }
</style>
</head>
<body>
  <main class="label">
    <div class="label__texture" role="img" aria-label="Subtle dark honeycomb background pattern"></div>
    <div class="band band--top"></div>
    <svg class="header-tab" viewBox="0 0 380 77" aria-hidden="true">
      <polygon points="0,0 380,0 362,77 18,77" fill="var(--gold)"/>
    </svg>
    <div class="brand-name">PERCH DYNAMICS</div>

    <h1 class="product-title">VITAMINS</h1>
    <p class="tagline">PERFORMANCE ENHANCING SUPPLEMENTS FOR RACING PIGEONS</p>
    <div class="series">XYZ Essential Series</div>
    <div class="series-letter">A</div>

    <div class="benefit-band"></div>
    <div class="brand-seal">PERCH<br>DYNAMICS</div>
    <p class="benefit-text">Supports Rigorous Training and Needs To Support Growth and Overall Well-being</p>

    <div class="band band--bottom"></div>
    <div class="capsule-badge">
      <svg width="184" height="101" viewBox="0 0 184 101" aria-hidden="true">
        <circle cx="94" cy="52" r="54" fill="var(--gold)"/>
        <rect x="0" y="65" width="184" height="36" fill="var(--gold)"/>
      </svg>
      <div class="capsule-badge__count">240</div>
      <div class="capsule-badge__unit">CAPSULES</div>
    </div>
  </main>
</body>
</html>
```